Vindmark Health & Wellness needs a fresh and interesting website

I need a rebrand and redevelopment of my website, www.dellaquorne.example
Our mission is provide bespoke , lifestyle medicine , everyone has their own path to health. and we are creating a personalized experience for people to life their life to the fullest
Vindmark - means sea lands
I need an landing page and about page and potentially a few project launch pages , I have been using Wordpress for my basic information and then I use Plovix for the launch pages of my programs since I can edit those easily.

Target Market(s)

Corporate and individual's who are interested in a different perspective on health and wellness , and living with a chronic illness

Industry/Entity Type

Health, lifestyle , wellness coaching and medicine

Coding

Number of Pages Required

Font styles to use
Other font styles liked:
• look into the logo

Requirements
Must have
• the logo I uploaded
Nice to have
• I want a fresh perspective on health, I have bamboo, hibiscus vibes in my logo , but also like more of a water vibe/ I want something earthy but not too boho it needs to be clean
Should not have
• every other holistic health vibe,

```html
<!DOCTYPE html>
<html lang="en">
<head>
<meta charset="utf-8">
<title>Vindmark Health &amp; Wellness</title>
<link href="https://fonts.googleapis.com/css2?family=Playfair+Display:wght@600;700&family=Poppins:wght@400;500;600&family=Montserrat:wght@400&display=swap" rel="stylesheet">
<style>
:root{
  --green:#5ba80c;
  --green-dark:#3f8a06;
  --blue:#0e6593;
  --teal-title:#1d6a8e;
  --text:#555;
  --beige:#f1ebe6;
  --white:#fff;
}
*{box-sizing:border-box;margin:0;padding:0}
html,body{width:1200px;height:3290px;overflow:hidden}
body{position:relative;background:var(--white);font-family:'Poppins',sans-serif;color:var(--text)}
.abs{position:absolute}
.serif{font-family:'Playfair Display',serif}
.btn{position:absolute;display:flex;align-items:center;justify-content:center;border-radius:30px;color:#fff;font-weight:600;font-size:15px;background:linear-gradient(90deg,var(--green),var(--blue));letter-spacing:.2px}

/* hero */
.hero{position:absolute;left:0;top:0;width:1200px;height:690px;background:radial-gradient(ellipse at 60% 40%,#a6d84a 0%,#76b92c 45%,#3f8a1c 100%);overflow:hidden}
.hero-photo{position:absolute;left:720px;top:140px;width:300px;height:440px;border-radius:150px 150px 0 0;background:linear-gradient(180deg,#c9a893,#d8c2c4 60%,#c7b0b6)}
.bamboo-strip{position:absolute;left:0;top:60px;width:110px;height:520px;background:linear-gradient(90deg,#2f6d12,#4c8f22 60%,transparent)}
.brand-top{position:absolute;left:124px;top:70px;width:190px;text-align:center;color:#fff}
.brand-top .name{font-family:'Playfair Display',serif;font-size:40px;font-weight:600;line-height:1}
.brand-top .sub{font-size:10px;letter-spacing:4px;margin-top:6px}
.nav{position:absolute;top:80px;left:414px;display:flex;gap:0;color:#fff;font-weight:500;font-size:16px}
.nav span{margin-right:42px}
.call{position:absolute;left:866px;top:28px;color:#fff;font-size:20px;font-weight:600;display:flex;align-items:center;gap:8px}
.hero-mark{position:absolute;left:135px;top:285px;width:185px;height:150px;border:5px solid #fff;border-radius:50%}
.hero-title{position:absolute;left:347px;top:300px;color:#fff}
.hero-title .big{font-family:'Playfair Display',serif;font-size:62px;font-weight:700;line-height:1}
.hero-title .small{font-size:29px;font-weight:600;letter-spacing:.5px;margin-top:2px}
.quote-btn{left:347px;top:415px;width:200px;height:50px;border:2px solid #fff;background:var(--green-dark);font-size:15px}

/* about */
.about-photo{position:absolute;left:212px;top:770px;width:362px;height:362px;border-radius:50%;background:linear-gradient(160deg,#4b8a3a,#9b6a5a 50%,#8b3a3d)}
.about-ring{position:absolute;left:202px;top:758px;width:383px;height:383px;border-radius:50%;border:2px solid var(--green)}
.flower{position:absolute;left:115px;top:955px;width:200px;height:215px;border-radius:50%;background:radial-gradient(circle at 45% 45%,#e5231f,#b8160f 55%,#2d6a1c 80%,transparent 81%)}
.about-title{position:absolute;left:641px;top:775px;color:var(--teal-title);font-size:40px;font-weight:600;line-height:1.2}
.about-text{position:absolute;left:641px;top:890px;width:390px;font-family:'Montserrat',sans-serif;font-size:15px;line-height:21px;color:#444}
.read-btn{left:643px;top:1062px;width:146px;height:48px}

/* services */
.services-bg{position:absolute;left:0;top:1220px;width:1200px;height:560px}
.section-title{position:absolute;width:1200px;text-align:center;color:var(--teal-title);font-family:'Playfair Display',serif;font-size:44px;font-weight:600}
.svc{position:absolute;width:220px;text-align:center}
.svc .icon{width:128px;height:128px;margin:0 auto;border-radius:50%;background:#fff;display:flex;align-items:center;justify-content:center}
.svc h3{font-size:17px;font-weight:500;color:#444;margin-top:17px}
.svc p{font-family:'Montserrat',sans-serif;font-size:15px;line-height:21px;margin-top:10px;color:#555}
.side-bamboo{position:absolute;left:0;top:1235px;width:80px;height:330px;background:linear-gradient(90deg,#4f9a1a,#8cc63a 70%,transparent)}
.side-hibiscus{position:absolute;left:1090px;top:1520px;width:110px;height:120px;border-radius:60px 0 0 60px;background:radial-gradient(circle at 60% 50%,#e8231d,#b5140f 70%)}

/* programs */
.card{position:absolute;top:1928px;width:286px;height:373px;background:#fff;box-shadow:0 3px 10px rgba(0,0,0,.12);text-align:center}
.card .img{height:194px}
.card h4{font-family:'Playfair Display',serif;font-size:19px;font-weight:600;color:#333;margin-top:32px}
.card p{font-family:'Montserrat',sans-serif;font-size:15px;line-height:21px;margin:24px 24px 0;color:#555}

/* contact */
.contact-bg{position:absolute;left:0;top:2370px;width:1200px;height:560px;background:linear-gradient(90deg,#e6f3cf 0%,#fbfdf6 35%,#fff 60%)}
.bamboo-photo{position:absolute;left:0;top:2480px;width:287px;height:420px;background:linear-gradient(100deg,#3e8a18,#8dc63f 55%,rgba(220,240,190,0))}
.contact-title{position:absolute;left:298px;top:2490px;color:var(--teal-title);font-size:56px;font-weight:700}
.contact-text{position:absolute;left:308px;top:2572px;width:410px;font-family:'Montserrat',sans-serif;font-size:15px;line-height:21px;color:#444}
.field{position:absolute;left:314px;width:393px;border-bottom:1px solid #bbb;font-size:14px;color:#444;padding-bottom:8px}
.submit-btn{left:313px;top:2826px;width:119px;height:41px;font-family:'Playfair Display',serif;font-size:15px}

/* footer */
.footer-brand{position:absolute;left:0;top:3030px;width:1200px;text-align:center;color:#fff}
.footer-brand .name{font-family:'Playfair Display',serif;font-size:58px;font-weight:600;line-height:1}
.footer-brand .sub{font-size:14px;letter-spacing:8px;margin-top:4px}
.footer-mark{position:absolute;left:560px;top:2942px;width:80px;height:80px;border-radius:50%;border:3px solid #fff}
.footer-rule{position:absolute;left:271px;top:3150px;width:657px;height:1px;background:rgba(255,255,255,.5)}
.footer-nav{position:absolute;left:271px;top:3184px;width:657px;display:flex;justify-content:space-between;color:#fff;font-size:16px}
.copyright{position:absolute;left:0;top:3228px;width:1200px;text-align:center;color:#fff;font-size:14px}
.social{position:absolute;left:40px;width:36px;height:36px;border-radius:50%;border:2px solid var(--green);background:var(--blue)}
.vertical-call{position:absolute;left:1108px;top:3040px;color:#fff;font-size:20px;font-weight:600;writing-mode:vertical-rl;display:flex;align-items:center;gap:8px}
</style>
</head>
<body>

<!-- Hero -->
<section class="hero">
  <div class="bamboo-strip" role="img" aria-label="Bamboo stalks in soft focus"></div>
  <div class="hero-photo" role="img" aria-label="Woman breathing fresh air with eyes closed"></div>
  <svg class="abs" style="left:0;top:520px" width="1200" height="170" viewBox="0 0 1200 170">
    <path d="M0,20 C120,100 300,150 480,145 C700,140 900,80 1200,40 L1200,170 L0,170Z" fill="#0e6593"/>
    <path d="M0,90 C150,140 330,170 520,165 C720,160 950,95 1200,65 L1200,170 L0,170Z" fill="#fff"/>
    <path d="M440,152 C700,112 950,32 1200,35 L1200,64 C950,70 720,140 440,152Z" fill="#5ba80c"/>
  </svg>
</section>

<header>
  <div class="brand-top"><div class="name">VINDMARK</div><div class="sub">HEALTH &amp; WELLNESS</div></div>
  <nav class="nav"><span>Home</span><span>About</span><span>Services</span><span>Fall Mini Retreat</span><span>Programs</span><span>Contact</span></nav>
  <div class="call">
    <svg width="24" height="24" viewBox="0 0 24 24" fill="none" stroke="#fff" stroke-width="1.8"><path d="M5 3h4l2 5-3 2a12 12 0 0 0 6 6l2-3 5 2v4a2 2 0 0 1-2 2A18 18 0 0 1 3 5a2 2 0 0 1 2-2z"/></svg>
    Call: 00X 551240
  </div>
</header>

<div class="hero-mark"></div>
<div class="hero-title">
  <div class="big">VINDMARK</div>
  <div class="small">HEALTH &amp; WELLNESS</div>
</div>
<div class="btn quote-btn">REQUEST A QUOTE</div>

<!-- About -->
<section class="about">
  <div class="about-ring"></div>
  <div class="about-photo" role="img" aria-label="Portrait of the practitioner in a red hat and scarf among green grasses"></div>
  <div class="flower" role="img" aria-label="Red hibiscus flowers"></div>
  <h1 class="about-title serif">Dr Della P Quorne<br>DACM, L.Ac.</h1>
  <p class="about-text">At a young age, I discovered the transformative power of Eastern Medicine when it helped me overcome lung concerns, propelling me toward my dreams as a young athlete. Years later, I faced a pivotal choice: How could I best serve and heal my community? The answer was crystal clear—Eastern Medicine.</p>
  <div class="btn read-btn">READ MORE</div>
</section>

<!-- Services -->
<svg class="services-bg" viewBox="0 0 1200 560">
  <defs><linearGradient id="svcGrad" x1="0" y1="0" x2="0" y2="1"><stop offset="0" stop-color="#f3ece7"/><stop offset="1" stop-color="#eef0f1"/></linearGradient></defs>
  <path d="M0,90 Q600,-60 1200,90 L1200,480 Q600,620 0,470Z" fill="url(#svcGrad)"/>
</svg>
<div class="side-bamboo" role="img" aria-label="Bamboo stem with leaves"></div>
<div class="side-hibiscus" role="img" aria-label="Red hibiscus flower"></div>
<h2 class="section-title" style="top:1304px">Services</h2>

<div class="svc" style="left:120px;top:1404px">
  <div class="icon"><svg width="64" height="64" viewBox="0 0 64 64" fill="none" stroke="#3f8a06" stroke-width="2"><rect x="8" y="8" width="22" height="14" rx="6"/><rect x="32" y="14" width="22" height="14" rx="6" stroke="#0e6593"/><circle cx="18" cy="38" r="5"/><path d="M9 56a9 9 0 0 1 18 0z"/><circle cx="44" cy="38" r="5" stroke="#0e6593"/><path d="M35 56a9 9 0 0 1 18 0z" stroke="#0e6593"/></svg></div>
  <h3>Bespoke</h3>
  <p>Lorem ipsum dolor sam consectetur adipiscing eli sed do eiusmod temo.</p>
</div>
<div class="svc" style="left:375px;top:1404px">
  <div class="icon"><svg width="64" height="64" viewBox="0 0 64 64" fill="none" stroke="#3f8a06" stroke-width="2"><path d="M8 32h48a24 18 0 0 1-48 0z"/><path d="M24 52h16" stroke="#0e6593"/><path d="M36 30l16-22" stroke="#0e6593" stroke-width="4"/><path d="M20 30c-4-6-2-12 2-14 2 6 1 10-2 14zM28 30c0-6 3-10 7-11 0 5-3 9-7 11z"/></svg></div>
  <h3>Lifestyle Medicine</h3>
  <p>Lorem ipsum dolor sam consectetur adipiscing eli sed do eiusmod temo.</p>
</div>
<div class="svc" style="left:624px;top:1404px">
  <div class="icon"><svg width="64" height="64" viewBox="0 0 64 64" fill="none" stroke="#3f8a06" stroke-width="2"><path d="M20 58V46c-6-4-10-10-10-18a22 22 0 0 1 44 0l4 8h-5v8h-8v14" stroke="#0e6593"/><path d="M32 36c-5-4-5-10 0-16 5 6 5 12 0 16zM32 36c-8 0-12-4-12-10 6 0 10 3 12 10zM32 36c8 0 12-4 12-10-6 0-10 3-12 10z"/></svg></div>
  <h3>Wellness Coaching</h3>
  <p>Lorem ipsum dolor sam consectetur adipiscing eli sed do eiusmod temo.</p>
</div>
<div class="svc" style="left:864px;top:1404px">
  <div class="icon"><svg width="64" height="64" viewBox="0 0 64 64" fill="none" stroke="#3f8a06" stroke-width="2"><path d="M20 58V46c-6-4-10-10-10-18a22 22 0 0 1 44 0l4 8h-5v8h-8v14" stroke="#0e6593"/><circle cx="32" cy="26" r="12"/><path d="M32 32l-6-6a3.5 3.5 0 0 1 6-4 3.5 3.5 0 0 1 6 4z"/></svg></div>
  <h3>Health</h3>
  <p>Lorem ipsum dolor sam consectetur adipiscing eli sed do eiusmod temo.</p>
</div>

<!-- Programs -->
<h2 class="section-title" style="top:1850px">My Programs</h2>
<article class="card" style="left:125px">
  <div class="img" role="img" aria-label="Seashell on a sandy beach under a blue sky" style="background:linear-gradient(180deg,#9cc5e0 0%,#d8e5ec 40%,#d9c4a5 55%,#c8ab85 100%)"></div>
  <h4>Lorem Ipsum Dumy</h4>
  <p>Lorem ipsum dolor sit ame consectetur adipisc ing elitsed do eiusmod tempor inc.</p>
</article>
<article class="card" style="left:457px">
  <div class="img" role="img" aria-label="Stack of smooth balancing stones" style="background:linear-gradient(180deg,#b9c3c8 0%,#8f8a80 50%,#5e5a52 100%)"></div>
  <h4>Lorem Ipsum Dumy</h4>
  <p>Lorem ipsum dolor sit ame consectetur adipisc ing elitsed do eiusmod tempor inc.</p>
</article>
<article class="card" style="left:787px">
  <div class="img" role="img" aria-label="Person in a straw hat relaxing in the sun" style="background:linear-gradient(135deg,#e9b45a 0%,#d9a074 50%,#a4574a 100%)"></div>
  <h4>Lorem Ipsum Dumy</h4>
  <p>Lorem ipsum dolor sit ame consectetur adipisc ing elitsed do eiusmod tempor inc.</p>
</article>

<!-- Contact -->
<section>
  <div class="contact-bg"></div>
  <svg class="abs" style="left:0;top:2370px" width="1200" height="130" viewBox="0 0 1200 130">
    <path d="M0,0 L1200,0 L1200,20 C900,-5 500,20 0,110Z" fill="#fff"/>
    <path d="M0,110 C500,20 900,-5 1200,20 L1200,110 C950,40 600,50 0,120Z" fill="#5ba80c"/>
  </svg>
  <div class="bamboo-photo" role="img" aria-label="Green bamboo shoots with leaves in soft light"></div>
  <h2 class="contact-title serif">Conatct Us</h2>
  <p class="contact-text">Lorem ipsum dolor sit amet, consectetur adipiscing elit, sed doeiusmod tempor incididunt</p>
  <div class="field" style="top:2624px">Name:</div>
  <div class="field" style="top:2673px">Phone:</div>
  <div class="field" style="top:2736px;padding-bottom:32px;width:383px">Message:</div>
  <div class="btn submit-btn">SUBMIT</div>
</section>

<!-- Footer -->
<footer>
  <svg class="abs" style="left:0;top:2850px" width="1200" height="440" viewBox="0 0 1200 440">
    <path d="M0,40 C200,120 450,110 700,60 C900,20 1050,20 1200,60 L1200,440 L0,440Z" fill="#0e6593"/>
    <path d="M0,20 C200,100 450,95 700,48 C900,10 1050,10 1200,50 L1200,62 C1050,22 900,22 700,62 C450,112 200,122 0,42Z" fill="#5ba80c"/>
  </svg>
  <div class="footer-mark"></div>
  <div class="footer-brand"><div class="name">VINDMARK</div><div class="sub">HEALTH &amp; WELLNESS</div></div>
  <div class="footer-rule"></div>
  <nav class="footer-nav"><span>Home</span><span>About</span><span>Services</span><span>Fall Mini Retreat</span><span>Programs</span><span>Contact</span></nav>
  <p class="copyright">Vindmark Health &amp; Wellness © 2024 &nbsp;All rights reserved. Privacy Policy</p>
  <div class="social" style="top:3130px" aria-label="Social profile link"></div>
  <div class="social" style="top:3186px" aria-label="Social profile link"></div>
  <div class="vertical-call">
    <svg width="24" height="24" viewBox="0 0 24 24" fill="none" stroke="#fff" stroke-width="1.8" style="transform:rotate(90deg)"><path d="M5 3h4l2 5-3 2a12 12 0 0 0 6 6l2-3 5 2v4a2 2 0 0 1-2 2A18 18 0 0 1 3 5a2 2 0 0 1 2-2z"/></svg>
    Call: 00X 551240
  </div>
</footer>

</body>
</html>
```